Velmaran Business Card

Business card for philanthropic organization

Industry/Entity Type

Business

Contact Information for Business Card

Need a very ELEGANT, sober, embossed, formal business card... it should transmit CREDIBILITY. Not looking for a "fun card". would like white, grays or black designs.

Font styles to use
Script

Requirements
Must have
• Embossed look

```html
<!DOCTYPE html>
<html lang="en">
<head>
<meta charset="utf-8">
<title>Velmaran Business Card</title>
<link rel="stylesheet" href="https://fonts.googleapis.com/css2?family=Didact+Gothic&display=swap">
<style>
  :root {
    --backdrop: #d9d9d9;
    --card-white: #ffffff;
    --panel-light: #e6e6e6;
    --panel-mid: #b9b9bb;
    --panel-dark: #9c9c9f;
    --accent-amber: #e0962a;
    --text-gray: #8a8a8a;
    --text-dark: #2e2e2e;
    --fold-gray: #a9a9ab;
  }
  * { margin: 0; padding: 0; box-sizing: border-box; }
  html, body {
    width: 1200px;
    height: 1000px;
    overflow: hidden;
    background: var(--backdrop);
    font-family: "Didact Gothic", "Century Gothic", sans-serif;
  }
  .business-card {
    position: absolute;
    left: 100px;
    top: 217px;
    width: 1000px;
    height: 565px;
    background: var(--card-white);
    box-shadow: 0 6px 18px rgba(0,0,0,0.18);
    overflow: hidden;
  }
  .contact-panel {
    position: absolute;
    left: 512px;
    top: 0;
    width: 488px;
    height: 100%;
    background:
      radial-gradient(ellipse 260px 200px at 45% 62%, rgba(255,255,255,0.85), rgba(255,255,255,0) 70%),
      linear-gradient(160deg, var(--panel-dark) 0%, var(--panel-mid) 30%, var(--panel-light) 60%, var(--panel-mid) 100%);
  }
  .contact-list {
    position: absolute;
    right: 18px;
    top: 30px;
    list-style: none;
    text-align: right;
    color: var(--text-dark);
    font-size: 22px;
    line-height: 39.5px;
  }
  .org-mark {
    position: absolute;
    left: 30px;
    top: 90px;
    display: flex;
    align-items: center;
    gap: 12px;
    color: var(--accent-amber);
    font-size: 30px;
  }
  .org-mark-dot {
    width: 26px;
    height: 26px;
    border-radius: 50%;
    background: var(--accent-amber);
  }
  .holder-name {
    position: absolute;
    left: 48px;
    top: 210px;
    color: var(--accent-amber);
    font-size: 48px;
    font-weight: 400;
    letter-spacing: 0.5px;
  }
  .holder-role {
    position: absolute;
    left: 48px;
    top: 265px;
    color: var(--text-gray);
    font-size: 33px;
    line-height: 41px;
  }
  .corner-fold {
    position: absolute;
    left: 0;
    bottom: 0;
  }
</style>
</head>
<body>
  <div class="business-card">
    <div class="contact-panel">
      <ul class="contact-list">
        <li>0917-52208</li>
        <li>Panama, Republic of Panama</li>
        <li>+(000)-5550-1842</li>
        <li>tellivar@mailbox.example</li>
      </ul>
    </div>

    <div class="org-mark">
      <span class="org-mark-dot"></span>
      <span>Velmaran</span>
    </div>

    <h1 class="holder-name">Tomas Ellivar</h1>
    <p class="holder-role">Qadir Noor Velmaran<br>Potentate 2017</p>

    <svg class="corner-fold" width="120" height="100" viewBox="0 0 120 100" aria-hidden="true">
      <polygon points="0,0 0,100 110,100 72,62 26,62 26,20" fill="var(--fold-gray)" opacity="0.55"/>
      <polygon points="0,30 0,100 90,100 60,72 14,72 14,44" fill="var(--fold-gray)"/>
    </svg>
  </div>
</body>
</html>
```